Auto and Home Insurance Quote Letter

I am an insurance agent and i have been mailing out a front back auto and home insurance quotes in black and white to prospects in my area. I would like the letter to be updated with a new look and some new graphics that would help catch the attention of the prospects I am mailing to. Anything that would help the prospect to call my office.

```html
<!DOCTYPE html>
<html lang="en">
<head>
<meta charset="utf-8">
<title>Harbor Insurance Agency – Auto and Home Quote Letter</title>
<link href="https://fonts.googleapis.com/css2?family=Montserrat:ital,wght@0,400;0,500;0,600;0,700;0,800;1,400;1,600;1,700&display=swap" rel="stylesheet">
<style>
  :root{
    --ink:#222;
    --dark:#3a3a3a;
    --mid:#6b6b6b;
    --band:#d6d6d6;
    --row:#ececec;
    --bg:#e9e9e9;
    --paper:#fff;
    --sky:#bfe3f5;
    --sky-deep:#8fcbe8;
  }
  *{box-sizing:border-box;margin:0;padding:0}
  html,body{width:734px;height:1200px;overflow:hidden;background:var(--bg)}
  body{font-family:'Montserrat',sans-serif;color:var(--ink);position:relative}
  .icon-defs{position:absolute;width:0;height:0}

  .page{position:absolute;left:162px;width:410px;height:580px;background:var(--paper);
        box-shadow:0 3px 8px rgba(0,0,0,.25);overflow:hidden}
  .page--front{top:14px}
  .page--back{top:606px}

  /* header */
  .masthead{position:absolute;left:0;top:0;width:410px;height:60px}
  .masthead__shape{position:absolute;left:0;top:0}
  .agency-name{position:absolute;left:12px;top:22px;color:#fff;font-weight:600;font-size:8.5px;letter-spacing:.2px;text-transform:uppercase}
  .carrier{position:absolute;left:212px;top:11px;width:62px;display:flex;align-items:center;gap:3px}
  .carrier__dot{width:9px;height:9px;border:1.4px solid var(--ink);border-radius:50%;flex:none}
  .carrier__name{font-weight:700;font-size:7.6px;line-height:1.05;color:var(--ink)}
  .contact{position:absolute;left:282px;top:9px;width:122px;font-size:5.2px;font-weight:700;line-height:1.35}
  .contact__title{font-size:5.6px;margin-bottom:2px}
  .contact__row{display:flex;gap:7px;align-items:flex-start}
  .contact__row svg{width:5px;height:5px;flex:none;margin-top:1px}
  .contact__row span{font-size:4.4px}

  .recipient{position:absolute;left:22px;top:64px;font-size:6px;font-weight:700;line-height:1.6}

  /* front body */
  .headline{position:absolute;left:22px;top:124px;width:366px;font-size:8.6px;font-weight:800;line-height:1.3}
  .intro{position:absolute;left:22px;top:162px;width:366px;font-size:5.5px;line-height:1.35;color:#444}
  .premium{position:absolute;left:22px;top:201px;width:170px}
  .premium__title{font-size:11px;font-weight:700;line-height:1.15}
  .pill{display:inline-block;background:var(--dark);color:#fff;font-size:10px;font-weight:700;padding:1px 14px 1px 4px;border-radius:8px}
  .driver{margin-top:20px;margin-left:8px;font-size:10px;font-weight:700;border-bottom:1px dashed #999;display:inline-block;padding-right:30px}
  .savings{position:absolute;left:215px;top:204px;width:170px;height:92px;border-radius:3px;box-shadow:0 1px 3px rgba(0,0,0,.25);overflow:hidden}
  .savings__art{position:absolute;inset:0;background:linear-gradient(180deg,var(--sky) 0%,var(--sky-deep) 100%)}
  .savings__text{position:absolute;left:0;right:0;bottom:4px;text-align:center;line-height:1.05}
  .savings__big{font-size:12px;font-weight:800;color:#6e6e6e;letter-spacing:.5px}
  .savings__sub{font-size:6.6px;font-weight:800;color:#5a6b3a}
  .savings__small{font-size:4.6px;font-weight:700;color:#222}

  /* tables */
  .rate-table{position:absolute;left:22px;width:366px;border-collapse:collapse;font-size:5.4px}
  .rate-table th{background:var(--dark);color:#fff;font-size:8.6px;font-weight:700;text-align:left;padding:3px 10px 2px;height:21px}
  .rate-table th:first-child{border-top-left-radius:8px}
  .rate-table th:last-child{border-top-right-radius:8px}
  .rate-table td{height:16px;padding:0 12px;font-weight:600;border-left:1px solid #c8c8c8}
  .rate-table td:first-child{border-left:none}
  .rate-table tbody tr:nth-child(odd) td{background:var(--row)}
  .rate-table tfoot td{height:6px;border:none;border-bottom:2px solid var(--dark);background:none;border-radius:0 0 8px 8px}
  .auto-table{top:316px}
  .auto-table col.c1{width:30%} .auto-table col.c2{width:39%} .auto-table col.c3{width:31%}
  .auto-table .limit,.auto-table .val{color:#555;font-weight:400}
  .auto-table .limit{text-align:center}
  .auto-table .strong{font-weight:700;color:var(--ink)}
  .auto-table .tiny{font-size:4.6px;font-weight:700}

  .disclaimer{position:absolute;left:22px;top:490px;width:366px;font-size:3.9px;line-height:1.4;color:#444}
  .opt-out{position:absolute;left:24px;top:541px;font-size:4.1px;font-style:italic;font-weight:600}

  .footer{position:absolute;left:0;right:0;bottom:0;height:22px;border-bottom:4px solid var(--dark);
          display:flex;align-items:center;padding:0 20px 2px;font-style:italic;font-weight:700;font-size:8.5px}
  .footer svg{width:8px;height:8px;margin-right:2px}
  .footer__phone{display:flex;align-items:center;width:120px}
  .footer__sep{width:1px;height:9px;background:var(--ink);margin-right:28px}
  .footer__place{display:flex;align-items:center;font-size:7.6px}
  .footer__place svg{margin-right:8px}

  /* back body */
  .pitch{position:absolute;left:22px;top:118px;width:366px;font-size:7.8px;font-weight:800;line-height:1.3}
  .example-tag{position:absolute;left:22px;top:163px;width:356px;height:16px;background:var(--band);border-radius:6px;
               font-size:6px;font-weight:700;letter-spacing:.3px;display:flex;align-items:center;padding-left:6px;color:#333}
  .home-facts{position:absolute;left:26px;top:188px;font-size:8.2px;font-weight:600;color:#333;word-spacing:1px}
  .home-facts b{font-weight:400;margin:0 6px}
  .home-table{top:228px}
  .home-table col.c1{width:33%} .home-table col.c2{width:67%}
  .home-table td{font-size:6px;height:18px}
  .home-table td:first-child{padding-left:12px}
  .home-table tfoot td{height:8px}
  .badge{position:absolute;left:240px;top:274px;width:124px;height:100px}
  .badge__text{position:absolute;left:240px;top:299px;width:124px;text-align:center;color:#fff;font-weight:600;font-size:6.6px;line-height:1.1}
  .badge__amount{display:block;font-size:12px;font-weight:700;margin-top:2px}
  .quote-note{position:absolute;left:25px;top:413px;width:360px;font-size:4.9px;font-style:italic;font-weight:600;line-height:1.35}
  .closing{position:absolute;left:25px;top:437px;font-size:6.8px;font-style:italic;font-weight:600}
  .signature{position:absolute;left:26px;top:451px;width:80px;height:32px;background:linear-gradient(90deg,#f2f2f2,#e4e4e4);border-radius:2px}
  .signer{position:absolute;left:28px;top:491px;font-size:6.8px;font-weight:700;line-height:1.35;color:#333}
  .roof-box{position:absolute;left:200px;top:431px;width:185px;height:106px;background:var(--band);border-radius:4px;padding:12px 18px}
  .roof-box__title{font-size:9px;font-weight:700;line-height:1.2;color:#333}
  .roof-box__body{font-size:4.8px;line-height:1.35;margin-top:6px;color:#444}
  .roof-box__cta{font-size:8.5px;font-weight:700;margin-top:10px;color:#333}
</style>
</head>
<body>

<svg class="icon-defs" aria-hidden="true">
  <symbol id="i-phone" viewBox="0 0 24 24"><path fill="currentColor" d="M6.6 10.8a15 15 0 0 0 6.6 6.6l2.2-2.2a1 1 0 0 1 1-.25 11.4 11.4 0 0 0 3.6.57 1 1 0 0 1 1 1V20a1 1 0 0 1-1 1A17 17 0 0 1 3 4a1 1 0 0 1 1-1h3.5a1 1 0 0 1 1 1c0 1.25.2 2.45.57 3.57a1 1 0 0 1-.25 1z"/></symbol>
  <symbol id="i-pin" viewBox="0 0 24 24"><path fill="currentColor" d="M12 2a7 7 0 0 0-7 7c0 5.2 7 13 7 13s7-7.8 7-13a7 7 0 0 0-7-7zm0 9.5A2.5 2.5 0 1 1 12 6.5a2.5 2.5 0 0 1 0 5z"/></symbol>
  <symbol id="i-mail" viewBox="0 0 24 24"><path fill="currentColor" d="M3 5h18v14H3zm2 2v.5l7 4.5 7-4.5V7z"/></symbol>
  <symbol id="i-globe" viewBox="0 0 24 24"><circle cx="12" cy="12" r="9" fill="none" stroke="currentColor" stroke-width="2.4"/><path d="M3 12h18M12 3c3 3 3 15 0 18M12 3c-3 3-3 15 0 18" fill="none" stroke="currentColor" stroke-width="2"/></symbol>
</svg>

<!-- FRONT: auto quote -->
<section class="page page--front">
  <header class="masthead">
    <svg class="masthead__shape" width="410" height="60" viewBox="0 0 410 60" aria-hidden="true">
      <path fill="#3a3a3a" d="M0 0H410V6H232C208 6 202 18 192 34C182 50 172 56 150 56H0Z"/>
    </svg>
    <div class="agency-name">Harbor Insurance Agency</div>
    <div class="carrier"><span class="carrier__dot"></span><span class="carrier__name">Keystone<br>Mutual</span></div>
    <div class="contact">
      <div class="contact__title">Sample Auto Insurance Quote<br>¡Hablamos Español!</div>
      <div class="contact__row"><svg><use href="#i-pin"/></svg><span>Harbor Insurance Agency, Inc.<br>Orlando, FL</span></div>
      <div class="contact__row"><svg><use href="#i-phone"/></svg><span>407-555-0182</span></div>
      <div class="contact__row"><svg><use href="#i-mail"/></svg><span>DHarbor@KeystoneMutual.com</span></div>
      <div class="contact__row"><svg><use href="#i-globe"/></svg><span>HarborInsAgency.com</span></div>
    </div>
  </header>

  <address class="recipient" style="font-style:normal">«FullName»<br>«Address» «Address2»<br>«City», «State» «Zip»</address>

  <h1 class="headline">Are You Paying Too Much for Auto Insurance? If I Cannot Save You Money On Your Auto and Home Insurance, Then I Will Give You $25 Just For Calling in For a Quote!</h1>
  <p class="intro">My goal is to keep my clients' premiums as low as possible without sacrificing coverage in addition to giving exceptional service. People who switch HIA have saved on average of $446 annually in the state of Florida! Below is a sample auto quote based on public information. Please call us at 407-555-0182 to discuss your specific driver, vehicle, and coverage information.</p>

  <div class="premium">
    <div class="premium__title">Your Monthly Estimated<br>Premium**</div>
    <span class="pill">Monthly</span><br>
    <span class="driver">Driver: «FullName»</span>
  </div>

  <div class="savings">
    <div class="savings__art" role="img" aria-label="Illustration of a house plus a yellow car, representing home and auto bundle savings"></div>
    <div class="savings__text">
      <div class="savings__big">SAVINGS</div>
      <div class="savings__sub">Combine and Save!</div>
      <div class="savings__small">Switch your home and car to HIA today<br>to take advantage of additional discounts</div>
    </div>
  </div>

  <table class="rate-table auto-table">
    <colgroup><col class="c1"><col class="c2"><col class="c3"></colgroup>
    <thead><tr><th>Coverages</th><th style="padding-left:30px">Coverage Limits</th><th style="padding-left:22px">«Vehicle1»</th></tr></thead>
    <tbody>
      <tr><td>Bodily Injury</td><td class="limit">«BI1»</td><td class="val">«BIPrem1»</td></tr>
      <tr><td>Property Damage</td><td class="limit">«PD1»</td><td class="val">«PDPrem1»</td></tr>
      <tr><td>Medial Payments</td><td class="limit">«Medical1»</td><td class="val">«MedicalPrem1»</td></tr>
      <tr><td>Collision</td><td class="limit">«Coll1»</td><td class="val">«CollDed1»</td></tr>
      <tr><td>Comprehensive</td><td class="limit">«Comp1»</td><td class="val">«CompDed1»</td></tr>
      <tr><td></td><td class="strong" style="padding-left:40px">Premium**</td><td class="strong">«Premium1»</td></tr>
      <tr><td></td><td class="strong" style="padding-left:40px;line-height:1.1">Six Month Estimated<br>Premium **</td><td class="strong">«Premium»</td></tr>
      <tr><td></td><td></td><td class="tiny">With Taxes and Surcharges</td></tr>
    </tbody>
    <tfoot><tr><td colspan="3"></td></tr></tfoot>
  </table>

  <p class="disclaimer">**Premium amounts shown are for a new six month policy and are for illustration only. Your actual premium will vary depending on a variety of factors that may include, but are not necessarily limited to, the coverage and deductible you select, eligibility requirements, credit history, driving record, applicable discounts, vehicle type and characteristics, and the number of miles driven annually. Coverage and discounts subject to terms, qualifications and availability. Insurance policies are not packaged. Each policy is separate and has its own limitations and restrictions. This quote is not a contract or binder of insurance. To apply for insurance you must complete the application process.</p>
  <p class="opt-out">If you no longer wish to receive mail solicitations from HIA, please call 407-555-0182.</p>

  <footer class="footer">
    <span class="footer__phone"><svg><use href="#i-phone"/></svg>407-555-0182</span>
    <span class="footer__sep"></span>
    <span class="footer__place"><svg><use href="#i-pin"/></svg>Orlando, FL • HarborInsAgency.com</span>
  </footer>
</section>

<!-- BACK: home quote -->
<section class="page page--back">
  <header class="masthead">
    <svg class="masthead__shape" width="410" height="60" viewBox="0 0 410 60" aria-hidden="true">
      <path fill="#3a3a3a" d="M0 0H410V6H232C208 6 202 18 192 34C182 50 172 56 150 56H0Z"/>
    </svg>
    <div class="agency-name">Harbor Insurance Agency</div>
    <div class="carrier"><span class="carrier__dot"></span><span class="carrier__name">Keystone<br>Mutual</span></div>
    <div class="contact">
      <div class="contact__title">Sample Auto Insurance Quote<br>¡Hablamos Español!</div>
      <div class="contact__row"><svg><use href="#i-pin"/></svg><span>Harbor Insurance Agency, Inc.<br>Orlando, FL</span></div>
      <div class="contact__row"><svg><use href="#i-phone"/></svg><span>407-555-0182</span></div>
      <div class="contact__row"><svg><use href="#i-mail"/></svg><span>DHarbor@KeystoneMutual.com</span></div>
      <div class="contact__row"><svg><use href="#i-globe"/></svg><span>HarborInsAgency.com</span></div>
    </div>
  </header>

  <address class="recipient" style="font-style:normal">«FullName»<br>«Address» «Address2»<br>«City», «State» «Zip»</address>

  <h2 class="pitch">If you are tired of paying too much for Home Insurance and want all your insurance needs handled under one agency, then call us at 407-555-0182. One call is all it takes to see if you've got the right coverage at the right price.</h2>
  <div class="example-tag">BELOW IS AN EXAMPLE OF A RECENT HOME INSURANCE POLICY IN ORLANDO</div>
  <p class="home-facts">Year Built: 2015<b>•</b>4 Bedrooms<b>•</b>Heated Square Feet: 2568</p>

  <table class="rate-table home-table">
    <colgroup><col class="c1"><col class="c2"></colgroup>
    <thead><tr><th>Coverages</th><th>Limits</th></tr></thead>
    <tbody>
      <tr><td>A - Dwelling Protection</td><td>$305,000.00</td></tr>
      <tr><td>B - Other Structures</td><td>6,100.00</td></tr>
      <tr><td>C - Personal Property</td><td>106,750.00</td></tr>
      <tr><td>D - Loss of Use</td><td>30,500.00</td></tr>
      <tr><td>E - Personal Liability</td><td>$300,000</td></tr>
      <tr><td>F - Medical Protection</td><td>$1,000.00</td></tr>
      <tr><td>AOP Deductible</td><td>$2,500</td></tr>
      <tr><td>Hurricane&nbsp; Deductible</td><td>2%</td></tr>
    </tbody>
    <tfoot><tr><td colspan="2"></td></tr></tfoot>
  </table>

  <svg class="badge" viewBox="0 0 124 100" aria-hidden="true">
    <polygon fill="#555" stroke="#9a9a9a" stroke-width="1.5" points="122,50 102.7,63 104.4,83.9 78.9,81.4 62,98 45.1,81.4 19.6,83.9 21.3,63 2,50 21.3,37 19.6,16.1 45.1,18.6 62,2 78.9,18.6 104.4,16.1 102.7,37"/>
  </svg>
  <div class="badge__text">Total Annual<br>Premium:<span class="badge__amount">$725.00</span></div>

  <p class="quote-note">The quoted premium is a sample premium based on a recent policy purchased in Orlando. Premium will differ based on information obtained on your application.</p>

  <p class="closing">Sincerely,</p>
  <div class="signature" role="img" aria-label="Handwritten signature of the agency principal"></div>
  <p class="signer">Daniel Harbor<br>&nbsp;Agency Principal</p>

  <aside class="roof-box">
    <div class="roof-box__title">Newer Roof ,<br>Save Even More</div>
    <p class="roof-box__body">If you have a newer roof , you may quality for addedsaving on your Keystone home home owners insurance</p>
    <div class="roof-box__cta">Ask Me Today!</div>
  </aside>

  <footer class="footer">
    <span class="footer__phone"><svg><use href="#i-phone"/></svg>407-555-0182</span>
    <span class="footer__sep"></span>
    <span class="footer__place"><svg><use href="#i-pin"/></svg>Orlando, FL • HarborInsAgency.com</span>
  </footer>
</section>

</body>
</html>
```